Established food business needs a new name card design

Refer to attached current name card. Would like a new professional look design with only the company name and logo without any pictures. Would like green and yellow to be included.
To include:
My name "HAKIM RUSLAN" and hand phone number "86207319".
To delete "
"Along Pinegrove Ave 3" and
"www.bu-tirah.com.sg"
To change email to:
"rvk27@tealmail.com.sg"

```html
<!DOCTYPE html>
<html lang="en">
<head>
<meta charset="utf-8">
<title>Bu-Tirah – Name Card</title>
<link rel="stylesheet" href="https://fonts.googleapis.com/css2?family=Montserrat:wght@500;700&display=swap">
<style>
  :root {
    --bg: #d9dadc;
    --green: #0f4433;
    --yellow: #f2d21b;
    --white: #ffffff;
    --shadow: 0 10px 24px rgba(0,0,0,.28);
  }
  * { margin: 0; padding: 0; box-sizing: border-box; }
  html, body { width: 1200px; height: 800px; overflow: hidden; }
  body { background: var(--bg); position: relative; font-family: "Montserrat", sans-serif; }

  .card {
    position: absolute;
    width: 580px; height: 331px;
    background: var(--green);
    box-shadow: var(--shadow);
    overflow: hidden;
  }
  .card--front { left: 520px; top: 50px; }
  .card--back  { left: 100px; top: 420px; }

  /* brand name set in the card's text font */
  .brand { position: absolute; display: flex; align-items: center; gap: 16px; }
  .brand__dot { width: 44px; height: 44px; border-radius: 50%; background: var(--yellow); flex: none; }
  .brand__name {
    font-family: "Montserrat", sans-serif; font-weight: 700;
    color: var(--yellow);
    font-size: 46px; line-height: 1; letter-spacing: 1px;
  }
  .card--front .brand { left: 50%; top: 50%; transform: translate(-50%, -50%); }

  /* back side */
  .back__edge {
    position: absolute; left: 0; top: 0; width: 70px; height: 100%;
    background: var(--white);
  }
  .back__disc {
    position: absolute; left: 20px; top: 18px;
    width: 260px; height: 260px; border-radius: 50%;
    background: var(--yellow);
  }
  .contact {
    position: absolute; right: 40px; top: 36px;
    text-align: right; color: var(--white);
  }
  .contact__name {
    color: var(--yellow); font-weight: 700;
    font-size: 19px; letter-spacing: 1px; margin-bottom: 14px;
  }
  .contact__address { font-weight: 500; font-size: 15px; line-height: 1.3; margin-bottom: 10px; }
  .contact__line {
    display: flex; justify-content: flex-end; align-items: center; gap: 8px;
    font-weight: 500; font-size: 15px; line-height: 1.5;
  }
  .contact__icon { width: 15px; height: 15px; flex: none; }
  .card--back .brand { right: 40px; bottom: 36px; }
  .card--back .brand__name { font-size: 32px; }
</style>
</head>
<body>

<section class="card card--front">
  <div class="brand">
    <span class="brand__dot"></span>
    <span class="brand__name">BU-TIRAH</span>
  </div>
</section>

<section class="card card--back">
  <div class="back__edge"></div>
  <div class="back__disc"></div>

  <div class="contact">
    <p class="contact__name">HAKIM RUSLAN</p>
    <p class="contact__address">18 Tembusu Industrial<br>Estate Road 5 # 02-07<br>Singapore 728410</p>
    <p class="contact__line">86207319
      <svg class="contact__icon" viewBox="0 0 24 24" aria-hidden="true"><path fill="#f2d21b" d="M6.6 10.8a15.1 15.1 0 0 0 6.6 6.6l2.2-2.2c.3-.3.7-.4 1-.2 1.1.4 2.3.6 3.6.6.6 0 1 .4 1 1V20c0 .6-.4 1-1 1A17 17 0 0 1 3 4c0-.6.4-1 1-1h3.5c.6 0 1 .4 1 1 0 1.2.2 2.4.6 3.6.1.3 0 .7-.2 1z"/></svg>
    </p>
    <p class="contact__line">rvk27@tealmail.com.sg
      <svg class="contact__icon" viewBox="0 0 24 24" aria-hidden="true"><rect x="2.5" y="5" width="19" height="14" fill="none" stroke="#f2d21b" stroke-width="2"/><path d="M2.5 5l9.5 8 9.5-8" fill="none" stroke="#f2d21b" stroke-width="2"/></svg>
    </p>
  </div>

  <div class="brand">
    <span class="brand__name">BU-TIRAH</span>
  </div>
</section>

</body>
</html>
```